Tidewell Venture Group
TVG Tidewell Venture Group
THE ONLY CHECK YOU WILL WRITE, WILL BE SMALLER THEN THE ONE YOU WROTE THE MONTH BEFORE.
Corporate
We are looking for a brochure design with the attached logo.
The brochure should reflect the professional nature of what we do and the colors and look should flow with the logo.
Looking for a tri fold and book type design.
Use the vector file for the logo.

```html
<!DOCTYPE html>
<html lang="en">
<head>
<meta charset="utf-8">
<title>Tidewell Venture Group – Tri-fold Brochure</title>
<link href="https://fonts.googleapis.com/css2?family=Open+Sans:wght@400;600;700;800&display=swap" rel="stylesheet">
<style>
  :root {
    --blue: #1b7fd4;
    --blue-light: #5db4ef;
    --blue-pale: #e6f2fc;
    --navy: #0c3474;
    --ink: #4a4f57;
    --muted: #8a9099;
    --paper: #ffffff;
    --bg: #eef0f2;
    --photo-a: #c9d6e3;
    --photo-b: #8ea4bb;
  }
  * { box-sizing: border-box; margin: 0; padding: 0; }
  html, body { width: 1200px; height: 899px; overflow: hidden; }
  body { background: var(--bg); font-family: "Open Sans", Arial, sans-serif; color: var(--ink); position: relative; }

  .spread { position: absolute; left: 30px; width: 720px; height: 420px; display: grid; grid-template-columns: repeat(3, 1fr); background: var(--paper); box-shadow: 0 2px 10px rgba(0,0,0,.15); }
  .spread--outside { top: 20px; }
  .spread--inside { top: 459px; }
  .panel { position: relative; overflow: hidden; border-right: 1px solid #e4e8ec; }
  .panel:last-child { border-right: 0; }

  .photo { position: absolute; left: 0; right: 0; background: linear-gradient(135deg, var(--photo-a), var(--photo-b)); }
  .swoosh { position: absolute; left: 0; width: 100%; display: block; }

  .heading { font-weight: 700; color: var(--blue); font-size: 17px; }
  .body-text { font-size: 7.5px; line-height: 1.55; color: var(--muted); margin-bottom: 8px; }

  .brand { color: var(--navy); font-weight: 800; text-align: center; }
  .brand__initials { font-size: 44px; letter-spacing: 2px; line-height: 1; }
  .brand__name { font-size: 11px; margin-top: 4px; }

  .tagline { color: #fff; font-weight: 600; text-transform: uppercase; line-height: 1.45; }

  /* outside */
  .event { padding: 22px 16px 0; }
  .event .heading { margin-bottom: 12px; }
  .cover-band { position: absolute; top: 0; left: 0; right: 0; height: 112px; background: linear-gradient(180deg, var(--blue), #0f64b8); padding: 16px 16px 0 14px; }
  .cover-band .tagline { font-size: 9px; }
  .contact { position: absolute; bottom: 0; left: 0; right: 0; height: 96px; background: linear-gradient(180deg, var(--blue), var(--navy)); padding: 20px 16px 0 70px; color: #fff; }
  .contact__title { font-weight: 700; font-size: 12px; margin-bottom: 6px; }
  .contact__text { font-size: 7px; line-height: 1.5; color: #dbeaf8; }

  /* inside */
  .about { background: linear-gradient(180deg, #fff 40%, var(--blue-pale)); }
  .about__band { position: absolute; top: 0; left: 0; right: 0; height: 58px; background: linear-gradient(90deg, var(--navy), var(--blue)); padding: 20px 16px 0; }
  .about__band .heading { color: #fff; }
  .about__body { position: absolute; top: 72px; left: 16px; right: 16px; }
  .checks { list-style: none; margin-top: 6px; }
  .checks li { display: flex; align-items: center; gap: 6px; font-size: 8px; color: var(--ink); margin-bottom: 7px; }
  .checks svg { flex: none; }

  .section { position: absolute; top: 122px; left: 16px; right: 14px; }
  .section .heading { margin-bottom: 10px; }
  .services li { list-style: none; display: flex; gap: 7px; font-size: 7.5px; line-height: 1.5; color: var(--muted); margin-bottom: 9px; }
  .services .bullet { flex: none; width: 9px; height: 9px; margin-top: 2px; background: var(--blue); border-radius: 2px; }
  .reach { position: absolute; bottom: 0; left: 0; right: 0; height: 70px; background: linear-gradient(180deg, var(--blue), var(--navy)); color: #fff; text-align: right; padding: 22px 16px 0; }
  .reach__phone { font-size: 14px; font-weight: 700; }
  .reach__web { font-size: 9px; }

  /* front cover */
  .front { position: absolute; left: 790px; top: 20px; width: 380px; height: 859px; background: var(--paper); overflow: hidden; box-shadow: 0 2px 10px rgba(0,0,0,.15); }
  .front .cover-band { height: 250px; padding: 36px 34px 0 30px; }
  .front .cover-band .tagline { font-size: 19px; }
  .front .brand { position: absolute; top: 320px; left: 0; right: 0; }
  .front .brand__initials { font-size: 86px; }
  .front .brand__name { font-size: 20px; margin-top: 6px; }
</style>
</head>
<body>

<!-- Outside spread -->
<section class="spread spread--outside" aria-label="Brochure outside">
  <div class="panel">
    <div class="event">
      <h2 class="heading">Event Management</h2>
      <p class="body-text">Our team plans every event with care, from the first call to the final guest leaving the room.</p>
      <p class="body-text">We handle venues, budgets and schedules so your people can focus on the work that matters most.</p>
    </div>
    <div class="photo" style="top:290px;bottom:0" role="img" aria-label="Photo of a businesswoman working at a laptop"></div>
    <svg class="swoosh" style="top:270px;height:50px" viewBox="0 0 240 50" preserveAspectRatio="none" aria-hidden="true">
      <path d="M0 0 H240 V18 C160 42 80 14 0 38 Z" fill="#fff"/>
      <path d="M0 38 C80 14 160 42 240 18 V24 C160 48 80 22 0 46 Z" fill="var(--blue)"/>
    </svg>
  </div>

  <div class="panel">
    <div class="photo" style="top:0;height:140px" role="img" aria-label="Photo of a business team meeting in an office"></div>
    <svg class="swoosh" style="top:118px;height:36px" viewBox="0 0 240 36" preserveAspectRatio="none" aria-hidden="true">
      <path d="M0 20 C90 0 170 30 240 8 V36 H0 Z" fill="#fff"/>
      <path d="M0 18 C90 -2 170 28 240 6 V12 C170 34 90 4 0 24 Z" fill="var(--blue-light)"/>
    </svg>
    <div class="brand" style="position:absolute;top:172px;left:0;right:0">
      <div class="brand__initials">TVG</div>
      <div class="brand__name">Tidewell Venture Group</div>
    </div>
    <div class="photo" style="top:280px;bottom:0" role="img" aria-label="Photo of a smiling customer service agent with a headset"></div>
    <svg class="swoosh" style="top:264px;height:34px" viewBox="0 0 240 34" preserveAspectRatio="none" aria-hidden="true">
      <path d="M0 0 H240 V10 C150 34 80 8 0 26 Z" fill="#fff"/>
      <path d="M0 26 C80 8 150 34 240 10 V16 C150 40 80 14 0 32 Z" fill="var(--blue)"/>
    </svg>
  </div>

  <div class="panel">
    <div class="cover-band">
      <p class="tagline">The only check you will write, will be smaller then the one you wrote the month before.</p>
    </div>
    <div class="photo" style="top:112px;height:220px" role="img" aria-label="Photo of a businessman presenting charts to colleagues"></div>
    <svg class="swoosh" style="top:98px;height:30px" viewBox="0 0 240 30" preserveAspectRatio="none" aria-hidden="true">
      <path d="M0 0 H240 V14 C160 0 90 28 0 10 Z" fill="#0f64b8"/>
      <path d="M0 10 C90 28 160 0 240 14 V20 C160 6 90 34 0 16 Z" fill="#fff"/>
    </svg>
    <div class="contact">
      <p class="contact__title">Contact Us Today!</p>
      <p class="contact__text">Call our advisers today for a free review of your plans and costs.</p>
    </div>
    <svg class="swoosh" style="bottom:82px;height:30px" viewBox="0 0 240 30" preserveAspectRatio="none" aria-hidden="true">
      <path d="M0 30 C70 0 160 24 240 4 V30 Z" fill="var(--blue)"/>
    </svg>
  </div>
</section>

<!-- Inside spread -->
<section class="spread spread--inside" aria-label="Brochure inside">
  <div class="panel about">
    <div class="about__band"><h2 class="heading">About Us</h2></div>
    <svg class="swoosh" style="top:48px;height:24px" viewBox="0 0 240 24" preserveAspectRatio="none" aria-hidden="true">
      <path d="M0 0 H240 V4 C150 24 70 2 0 16 Z" fill="var(--blue)"/>
    </svg>
    <div class="about__body">
      <p class="body-text">Tidewell Venture Group helps firms of every size grow with clear advice and steady support.</p>
      <p class="body-text">Our advisers bring years of hands-on experience in finance, planning and daily operations.</p>
      <ul class="checks">
        <li><svg width="11" height="11" viewBox="0 0 11 11" aria-hidden="true"><circle cx="5.5" cy="5.5" r="5.5" fill="var(--blue)"/><path d="M3 5.6 L4.8 7.3 L8 3.9" stroke="#fff" stroke-width="1.4" fill="none"/></svg>Clear monthly reports</li>
        <li><svg width="11" height="11" viewBox="0 0 11 11" aria-hidden="true"><circle cx="5.5" cy="5.5" r="5.5" fill="var(--blue)"/><path d="M3 5.6 L4.8 7.3 L8 3.9" stroke="#fff" stroke-width="1.4" fill="none"/></svg>Honest fixed pricing</li>
        <li><svg width="11" height="11" viewBox="0 0 11 11" aria-hidden="true"><circle cx="5.5" cy="5.5" r="5.5" fill="var(--blue)"/><path d="M3 5.6 L4.8 7.3 L8 3.9" stroke="#fff" stroke-width="1.4" fill="none"/></svg>Dedicated account team</li>
        <li><svg width="11" height="11" viewBox="0 0 11 11" aria-hidden="true"><circle cx="5.5" cy="5.5" r="5.5" fill="var(--blue)"/><path d="M3 5.6 L4.8 7.3 L8 3.9" stroke="#fff" stroke-width="1.4" fill="none"/></svg>Fast local support</li>
      </ul>
    </div>
  </div>

  <div class="panel">
    <div class="photo" style="top:0;height:108px" role="img" aria-label="Photo of hands reviewing documents on a meeting table"></div>
    <svg class="swoosh" style="top:92px;height:26px" viewBox="0 0 240 26" preserveAspectRatio="none" aria-hidden="true">
      <path d="M0 16 C90 0 160 24 240 6 V26 H0 Z" fill="#fff"/>
      <path d="M0 14 C90 -2 160 22 240 4 V9 C160 27 90 3 0 19 Z" fill="var(--blue)"/>
    </svg>
    <div class="section">
      <h2 class="heading">Services</h2>
      <ul class="services">
        <li><span class="bullet"></span>Business planning and growth strategy for new and growing firms.</li>
        <li><span class="bullet"></span>Cash flow reviews that lower your monthly costs.</li>
        <li><span class="bullet"></span>Payroll and bookkeeping handled by our team.</li>
        <li><span class="bullet"></span>Tax preparation with careful year-round planning.</li>
        <li><span class="bullet"></span>Risk checks that protect your assets and staff.</li>
      </ul>
    </div>
    <div class="photo" style="top:335px;bottom:0" role="img" aria-label="Photo of two colleagues working together at a desk"></div>
    <svg class="swoosh" style="top:322px;height:24px" viewBox="0 0 240 24" preserveAspectRatio="none" aria-hidden="true">
      <path d="M0 0 H240 V8 C150 24 80 4 0 18 Z" fill="#fff"/>
    </svg>
  </div>

  <div class="panel">
    <div class="photo" style="top:0;height:108px;background:linear-gradient(135deg,#dfe6ee,#a8b8c9)" role="img" aria-label="Photo of a hand pointing at a printed report"></div>
    <svg class="swoosh" style="top:92px;height:26px" viewBox="0 0 240 26" preserveAspectRatio="none" aria-hidden="true">
      <path d="M0 6 C80 24 160 0 240 16 V26 H0 Z" fill="#fff"/>
      <path d="M0 4 C80 22 160 -2 240 14 V19 C160 3 80 27 0 9 Z" fill="var(--blue)"/>
    </svg>
    <div class="section">
      <h2 class="heading">Mission</h2>
      <p class="body-text">Our mission is to lower what you pay each month while giving you more time to run your business.</p>
      <p class="body-text">We measure success by the savings our clients see, month after month, year after year.</p>
    </div>
    <svg class="swoosh" style="bottom:56px;height:30px" viewBox="0 0 240 30" preserveAspectRatio="none" aria-hidden="true">
      <path d="M0 30 C90 4 170 22 240 0 V30 Z" fill="var(--blue)"/>
    </svg>
    <div class="reach">
      <p class="reach__phone">(555) 214-0193</p>
      <p class="reach__web">www.tidewellvg.com</p>
    </div>
  </div>
</section>

<!-- Front cover -->
<section class="front" aria-label="Brochure front cover">
  <div class="cover-band">
    <p class="tagline">The only check you will write, will be smaller then the one you wrote the month before</p>
  </div>
  <svg class="swoosh" style="top:210px;height:80px" viewBox="0 0 380 80" preserveAspectRatio="none" aria-hidden="true">
    <path d="M0 0 H380 V30 C250 0 140 70 0 40 Z" fill="#0f64b8"/>
    <path d="M0 40 C140 70 250 0 380 30 V44 C250 14 140 84 0 54 Z" fill="#fff"/>
    <path d="M0 54 C140 84 250 14 380 44 V50 C250 20 140 90 0 60 Z" fill="var(--blue-light)"/>
  </svg>
  <div class="brand">
    <div class="brand__initials">TVG</div>
    <div class="brand__name">Tidewell Venture Group</div>
  </div>
  <div class="photo" style="top:490px;bottom:0" role="img" aria-label="Photo of a businessman presenting charts to colleagues"></div>
  <svg class="swoosh" style="top:470px;height:60px" viewBox="0 0 380 60" preserveAspectRatio="none" aria-hidden="true">
    <path d="M0 0 H380 V14 C250 50 120 10 0 40 Z" fill="#fff"/>
    <path d="M0 40 C120 10 250 50 380 14 V22 C250 58 120 18 0 48 Z" fill="var(--blue)"/>
  </svg>
  <svg class="swoosh" style="bottom:0;height:90px" viewBox="0 0 380 90" preserveAspectRatio="none" aria-hidden="true">
    <path d="M0 90 V40 C120 80 260 20 380 50 V90 Z" fill="var(--blue)"/>
    <path d="M0 30 C120 70 260 10 380 40 V46 C260 16 120 76 0 36 Z" fill="#fff"/>
  </svg>
</section>

</body>
</html>
```